Create a Awesome Email Banner - Promoting our LED Strip Lighting Range

Hi all,

We are an online lighting retailer and we need a stunning email banner. This will be used to promote to range of Bespoke, cut to size led strip lights.

It will point to this page:
brightvorn.co.uk/led-tape/led-tape-single-colour/led-tape-cut-to-size/
and also:
brightvorn.co.uk/led-tape/rgb-colour-changing-led-tape/

Email banner should be - 600x800px - + Shop Now Button

Banners should include the message "Bespoke, Cut to size LED Strip Lighting from only £14.95."

Please make sure that the banners match our website colour scheme. brightvorn.co.uk/

DO NOT INCLUDE OUR LOGO IN YOUR DESIGN

Please make your entry unique and creative and DO NOT copy other freelancers work.

If you have any questions then please use the clarification board but please DON'T use it to ask me to check your entry - ALL entries will be rated!

Thank you and GOOD LUCK!
(Dorvane)

```html
<!DOCTYPE html>
<html lang="en">
<head>
<meta charset="utf-8">
<title>Bespoke LED Strip Lighting – Email Banners</title>
<link rel="stylesheet" href="https://fonts.googleapis.com/css2?family=Montserrat:wght@500;700;800&display=swap">
<style>
  :root {
    --stage: #595959;
    --panel: rgba(10, 28, 48, 0.86);
    --accent: #f0a21c;
    --navy: #12243f;
    --cyan: #3fd3e6;
    --sample-light: #f4f4f6;
    --sample-shade: #d9dbe2;
  }
  * { box-sizing: border-box; margin: 0; padding: 0; }
  html, body { width: 1200px; height: 767px; overflow: hidden; }
  body {
    background: var(--stage);
    font-family: "Montserrat", Arial, sans-serif;
    position: relative;
  }
  .banner {
    position: absolute;
    top: 53px;
    width: 495px;
    height: 660px;
    overflow: hidden;
  }
  .banner--room { left: 49px; }
  .banner--office { left: 656px; }
  .banner__photo { position: absolute; inset: 0; }
  .banner--room .banner__photo {
    background:
      radial-gradient(ellipse 60% 45% at 30% 35%, #1a8fe0 0%, #0b4d9a 45%, transparent 80%),
      linear-gradient(180deg, #0b3f86 0%, #082e66 55%, #050f1e 80%, #03070d 100%);
  }
  .banner--office .banner__photo {
    background:
      radial-gradient(ellipse 70% 30% at 35% 10%, #4ce0ea 0%, transparent 70%),
      linear-gradient(180deg, #9fb3b8 0%, #7e9499 40%, #4c5a60 65%, #9aa6aa 85%, #b7c0c2 100%);
  }
  .offer__frame {
    position: absolute;
    left: 72px; top: 176px;
    width: 353px; height: 309px;
    border: 2px dashed var(--cyan);
    border-radius: 10px;
  }
  .offer {
    position: absolute;
    left: 82px; top: 186px;
    width: 335px; height: 293px;
    background: var(--panel);
    border-radius: 8px;
    color: var(--accent);
    text-align: center;
  }
  .offer__title {
    margin-top: 20px;
    font-size: 29px;
    line-height: 36px;
    font-weight: 500;
    letter-spacing: 0.3px;
  }
  .offer__title strong { font-weight: 700; }
  .offer__divider {
    position: absolute;
    left: 0; right: 0; top: 141px;
    height: 1px;
    background: var(--cyan);
  }
  .offer__lead {
    position: absolute;
    left: 0; right: 0; top: 146px;
    font-size: 27px;
    font-weight: 700;
    line-height: 30px;
  }
  .offer__price {
    position: absolute;
    left: 0; right: 0; top: 176px;
    font-size: 41px;
    font-weight: 800;
    line-height: 46px;
  }
  .offer__button {
    position: absolute;
    left: 81px; top: 234px;
    width: 172px; height: 34px;
    background: var(--accent);
    color: var(--navy);
    font-size: 21px;
    font-weight: 800;
    line-height: 34px;
    text-decoration: none;
  }
  .product-photo {
    position: absolute;
    top: 336px;
    width: 60px; height: 119px;
    border-radius: 5px;
    border: 2px solid #ffffff;
    background: linear-gradient(180deg, var(--sample-light) 0%, var(--sample-shade) 100%);
  }
  .product-photo--left { left: 86px; }
  .product-photo--right { left: 348px; }
</style>
</head>
<body>

  <section class="banner banner--room">
    <div class="banner__photo" role="img" aria-label="Dark living room wall washed in blue LED strip backlight behind a mounted screen"></div>
    <div class="offer__frame"></div>
    <div class="offer">
      <h1 class="offer__title">BESPOKE, CUT<br>TO SIZE <strong>LED<br>STRIP LIGHTING</strong></h1>
      <p class="offer__lead">FROM ONLY</p>
      <p class="offer__price">£14.95</p>
      <a class="offer__button" href="https://brightvorn.co.uk/led-tape/rgb-colour-changing-led-tape/">SHOP NOW</a>
    </div>
    <div class="product-photo product-photo--left" role="img" aria-label="Product photo of colour LED strip tape reels"></div>
    <div class="product-photo product-photo--right" role="img" aria-label="Product photo of colour LED strip tape reels"></div>
  </section>

  <section class="banner banner--office">
    <div class="banner__photo" role="img" aria-label="Modern meeting room with cyan LED cove lighting, glass table and black office chairs"></div>
    <div class="offer__frame"></div>
    <div class="offer">
      <h1 class="offer__title">BESPOKE, CUT<br>TO SIZE <strong>LED<br>STRIP LIGHTING</strong></h1>
      <div class="offer__divider"></div>
      <p class="offer__lead">FROM ONLY</p>
      <p class="offer__price">£14.95</p>
      <a class="offer__button" href="https://brightvorn.co.uk/led-tape/led-tape-single-colour/led-tape-cut-to-size/">SHOP NOW</a>
    </div>
  </section>

</body>
</html>
```